Masterfolien & mehr | Branche Gesundheit | Anschlussaufträge
Tolle Leistung, netter Kontakt, verdienter Gewinner!
Zielgruppe
Sonnquell ist Dienstleister im Bereich 'Betriebliches Gesundheitsmanagement'. Zielgruppe sind Unternehmen zahlreicher Branchen, die die Gesundheit ihrer Mitarbeiter untersuchen und verbessern wollen.
Aufgabenstellung
Bitte möglichst Startfolie, Folie mit Aufzählungen und Text und Folie mit Bild und Text und Kontaktfolie.
Beispieltexte und eine entsprechende Folienansicht habe ich beigefügt, das könnte helfen.
Die Präsentation soll als E-Mail-Anhang im Nachgang eines Akquiseanrufs genutzt werden und über Produkte und Lösungen informieren.
Bitte Farbgebung berücksichtigen. Blau: 90/51/0/0, grau dunkel: 68/51/58/30, grau hell: 40/33/49/1
Schriften: Offen für Vorschläge, möglichst freie Schriften oder klassische Linotype.
Wir würden den Gewinner gern mit weiteren Aufträgen versehen, z.B. die Vorlage mit vorgegebenen Inhalten füllen, Flussdiagramme erstellen, Schaubilder erstellen etc..

```html
<!DOCTYPE html>
<html lang="de">
<head>
<meta charset="utf-8">
<title>Handlungsfelder und Seminarthemen – Sonnquell</title>
<link rel="stylesheet" href="https://fonts.googleapis.com/css2?family=Oswald:wght@500;600&family=Arimo:wght@400;700&display=swap">
<style>
  :root {
    --brand-blue: #0b6cb5;
    --grey-dark: #4a4e49;
    --grey-light: #aca58c;
    --text: #111111;
    --white: #ffffff;
    --photo-dark: #3c3a3c;
    --photo-mid: #8a8c90;
    --photo-red: #c8232c;
  }
  * { margin: 0; padding: 0; box-sizing: border-box; }
  html, body { width: 1200px; height: 848px; overflow: hidden; background: var(--white); }
  .slide { position: relative; width: 1200px; height: 848px; background: var(--white); font-family: "Arimo", Arial, sans-serif; color: var(--text); }

  .title-band { position: absolute; left: 0; top: 52px; width: 974px; height: 84px; background: var(--brand-blue); }
  .title-band svg { position: absolute; left: 0; top: 32px; }
  .slide-title { position: absolute; left: 52px; top: 8px; font-family: "Oswald", sans-serif; font-weight: 600; font-style: italic; font-size: 45px; line-height: 64px; color: var(--white); letter-spacing: 0.2px; }

  .brand { position: absolute; left: 995px; top: 76px; display: flex; align-items: center; gap: 8px; }
  .brand-dot { width: 14px; height: 14px; border-radius: 50%; background: var(--grey-dark); }
  .brand-name { font-family: "Arimo", sans-serif; font-weight: 700; font-size: 26px; color: var(--grey-dark); }

  .intro { position: absolute; left: 54px; top: 208px; font-size: 21.5px; line-height: 34px; }
  .intro strong { font-weight: 700; }

  .topic-card { position: absolute; left: 54px; top: 441px; width: 920px; height: 258px; display: flex; }
  .topic-text { width: 598px; height: 100%; border: 2px solid var(--grey-light); border-top: none; border-bottom-width: 3px; }
  .topic-heading { height: 57px; margin: 0 -2px; background: var(--brand-blue); color: var(--white); font-weight: 700; font-size: 21px; line-height: 57px; padding-left: 33px; letter-spacing: 0.3px; }
  .topic-body { padding: 27px 0 0 29px; font-size: 15.5px; line-height: 24px; }
  .topic-photo { flex: 1; height: 100%; background: linear-gradient(100deg, var(--photo-dark) 0%, var(--photo-mid) 45%, #b9bcc0 60%, var(--photo-red) 80%, var(--photo-dark) 100%); }

  .footer { position: absolute; top: 772px; font-family: "Oswald", sans-serif; font-weight: 500; font-style: italic; font-size: 17px; color: var(--grey-dark); }
  .footer-company { left: 54px; }
  .footer-page { left: 1102px; }
</style>
</head>
<body>
<div class="slide">
  <header class="title-band">
    <svg width="12" height="20" viewBox="0 0 12 20" aria-hidden="true"><polygon points="0,0 11,10 0,20" fill="#ffffff"/></svg>
    <h1 class="slide-title">Handlungsfelder und Seminarthemen</h1>
  </header>

  <div class="brand">
    <span class="brand-dot"></span>
    <span class="brand-name">Sonnquell</span>
  </div>

  <p class="intro">
    Nach der Bedarfsbestimmung können <strong>Handlungsfelder</strong><br>
    und <strong>Seminarthemen</strong> abgeleitet werden. Folgende verhal-<br>
    tens- und verhältnisorientierte Maßnahmen können z.B. Be-<br>
    standteil eines Gesundheitsmanagements für Pharmarefe-<br>
    renten sein:
  </p>

  <section class="topic-card">
    <div class="topic-text">
      <h2 class="topic-heading">GESUNDHEITSTAG</h2>
      <p class="topic-body">
        Zum Einstieg bietet sich ein <strong>Gesundheitstag</strong> an.<br>
        Um Ihre Mitarbeiter für das Thema Gesundheit zu<br>
        sensibilisieren eignet sich die <strong>„Sonnquell- Inspektion</strong>“<br>
        mit unserem Gesundheitsmobil incl. umfassendes<br>
        Screening/Checkup (z.B. Biofeedback Stressanalyse,<br>
        Vita Scan Rückencheck)
      </p>
    </div>
    <div class="topic-photo" role="img" aria-label="Foto: Berater zeigt einem Kunden im Gesundheitsmobil Messergebnisse auf einem Bildschirm"></div>
  </section>

  <footer>
    <span class="footer footer-company">SONNQUELL UG | 2018</span>
    <span class="footer footer-page">02</span>
  </footer>
</div>
</body>
</html>
```